Modernize an Old Theme (One Page Simple Design)

So we have a older theme in our Shopping Cart software that people love to use. In an effort to modernize the theme and make it responsive, we are looking to have it re designed. This project should be very easy to complete and here are the details:

1. We only need the one, main page, actually designed and just the PSD created. We will have someone else cut it up and make it responsive.

2. The design should be modernized and include elements such as a slide show place holder and and updated product tiling look.

3. The current theme can be viewed here: http://demo.brightcart.example//index.php?theme=classic_black - We want it to look like the current theme with the 3 columns. The classic look just modernized.

4. The social buttons can be updated and placed in the footer if possible. We would like to use a twitter widget and facebook like widget like on this newer theme here http://demo.brightcart.example/index.php?theme=bigshop_responsive

5. Keep in mind that the main color (black) in #3 theme link being redesigned, needs to easily be changeable via css when we create the HTML so avoid textures or backgrounds that would prevent this from happening.

Important Note: We want it to look like the current theme example linked in the description above with the 3 columns. The classic black theme. We just want to make it more modern looking

Industry/Entity Type

Shopping

Number of Pages Required

1 page

Requirements
Must have
• See description.
Nice to have
• See description.
Should not have
• See description.

```html
<!DOCTYPE html>
<html lang="en">
<head>
<meta charset="utf-8">
<title>BrightCart 4.0 Demo Store</title>
<link href="https://fonts.googleapis.com/css2?family=Open+Sans:ital,wght@0,400;0,600;0,700;1,600&display=swap" rel="stylesheet">
<style>
:root{
  --main:#262626;
  --accent:#f58220;
  --accent-dark:#d9680c;
  --page:#e6e6e6;
  --panel:#ffffff;
  --line:#d6d6d6;
  --text:#333333;
  --muted:#8a8a8a;
  --sky-1:#2f7fd0;
  --sky-2:#6fb3ee;
  --link:#1b95e0;
  --fb:#3b5b99;
}
*{box-sizing:border-box;margin:0;padding:0}
html,body{width:1200px;height:2760px;overflow:hidden}
body{font-family:"Open Sans",Arial,sans-serif;color:var(--text);background:var(--page);font-size:14px;position:relative}
.topbar{height:34px;background:var(--main);display:flex;align-items:center;padding:0 24px;color:#fff;font-size:15px;font-weight:600;gap:28px}
.topbar .admin{margin-left:auto;background:#555;color:#fff;font-size:12px;padding:5px 12px;border-radius:3px}
.caret{font-size:10px;margin-left:4px}
.hero{height:214px;background:linear-gradient(180deg,var(--sky-1),var(--sky-2));position:relative;color:#fff}
.brand{position:absolute;left:40px;top:40px;width:210px;height:78px;background:#fff;border-radius:4px;display:flex;align-items:center;justify-content:center}
.brand .name{font-size:30px;font-weight:700;color:var(--main)}
.hero h1{position:absolute;left:320px;right:320px;top:24px;text-align:center;font-size:26px;font-style:italic;font-weight:600}
.hero .slot{position:absolute;right:40px;top:40px;width:250px;text-align:center;font-size:22px;font-weight:700;line-height:1.25;opacity:.85}
.nav{height:34px;background:var(--main);display:flex;align-items:center;justify-content:center;gap:14px;color:#fff;font-size:15px;font-weight:600}
.nav span.sep{color:#888}
.cols{position:absolute;top:292px;left:0;width:1200px}
.col{position:absolute;top:0}
.left{left:36px;width:250px}
.center{left:314px;width:590px}
.right{left:930px;width:236px}
.panel{background:var(--panel);border:1px solid var(--line);border-radius:4px;margin-bottom:26px;overflow:hidden}
.panel-head{background:var(--main);color:#fff;font-weight:700;font-size:14px;height:36px;display:flex;align-items:center;padding:0 12px;gap:10px}
.panel-head .ico{width:12px;height:12px;background:var(--accent);border-radius:2px}
.center .panel-head{justify-content:center}
.panel-body{padding:14px 16px}
.select{border:1px solid var(--line);border-radius:3px;height:32px;display:flex;align-items:center;justify-content:space-between;padding:0 10px;color:var(--muted);font-size:13px}
.links{list-style:none}
.links li{padding:6px 0;font-size:14px;display:flex;gap:10px;align-items:center;color:#444}
.links li::before{content:"";width:6px;height:6px;background:var(--accent);border-radius:50%;flex:none}
.small li{font-size:13px;color:var(--muted)}
.field{border:1px solid var(--line);border-radius:3px;height:32px;padding:0 10px;display:flex;align-items:center;color:#aaa;font-size:13px;margin-bottom:10px}
.btn{display:inline-flex;align-items:center;justify-content:center;background:var(--accent);color:#fff;font-weight:600;font-size:13px;border-radius:3px;height:32px;padding:0 14px}
.btn.full{display:flex;width:100%}
.btn.ghost{background:#fff;color:var(--accent);border:1px solid var(--accent)}
.center-text{text-align:center}
.note{font-size:13px;color:var(--muted);text-align:center;margin-bottom:6px}
.product{display:flex;gap:22px;padding:26px 24px;border-bottom:1px solid var(--line);height:324px}
.product:last-child{border-bottom:none}
.thumb{width:150px;flex:none}
.thumb .photo{width:150px;height:176px;border:1px solid var(--line);border-radius:3px;background:linear-gradient(160deg,#2b3440,#0e1319 70%,#1b6a86)}
.sku{font-size:12px;color:var(--muted);margin-top:10px}
.stars{color:var(--accent);font-size:16px;letter-spacing:2px}
.stars .off{color:#ccc}
.stock{font-size:13px;font-weight:700;margin-top:4px}
.info h3{font-size:15px;color:var(--accent-dark);font-weight:600;margin-bottom:8px}
.info p{font-size:12.5px;line-height:1.55;color:#666}
.price{color:var(--accent);font-weight:700;font-size:18px;margin:14px 0 10px}
.actions{display:flex;gap:12px}
.social-card{border:1px solid var(--line);margin:20px;border-radius:3px;padding:20px}
.page-row{display:flex;gap:14px;align-items:center}
.page-row .sq{width:64px;height:64px;background:#ccc;border-radius:3px}
.page-row b{font-size:20px;color:var(--fb)}
.like{display:inline-block;background:var(--fb);color:#fff;font-size:12px;padding:3px 10px;border-radius:3px;margin-top:6px}
.faces{display:flex;gap:8px;margin-top:14px}
.faces i{width:38px;height:38px;background:#d8dde6;border-radius:3px;display:block}
.tweet{display:flex;gap:14px;padding:22px 18px;border-top:1px solid var(--line)}
.tweet:first-child{border-top:none}
.tweet .av{width:44px;height:44px;border-radius:4px;background:#c9d3de;flex:none}
.tweet b{font-size:13px}
.tweet .handle{color:var(--muted);font-size:12px}
.tweet p{font-size:19px;line-height:1.4;margin-top:6px}
.tag{color:var(--link)}
.footer{position:absolute;left:0;top:2640px;width:1200px;height:60px;background:#555;color:#eee;font-size:13px;display:flex;align-items:center;justify-content:center}
.powered{position:absolute;left:0;top:2700px;width:1200px;height:60px;background:#fff;color:#666;font-size:13px;display:flex;align-items:center;justify-content:center}
.totop{position:absolute;right:14px;top:2656px;width:28px;height:28px;background:#333;border-radius:3px}
.sale-photo{width:150px;height:150px;margin:6px auto 10px;background:linear-gradient(180deg,#f4f4f4,#e2e2e2);border:1px solid var(--line)}
</style>
</head>
<body>
<header class="topbar">
  <span>BRIGHTCART 4 DEMO</span>
  <span>Choose Theme<span class="caret">▼</span></span>
  <span class="admin">View Admin Area</span>
</header>

<section class="hero" role="img" aria-label="Slideshow placeholder banner">
  <div class="brand"><span class="name">BrightCart</span></div>
  <h1>Welcome to Demo BrightCart 4.0 Store</h1>
  <div class="slot">INSERT SLIDER IMAGE HERE</div>
</section>

<nav class="nav"><span>Home</span><span class="sep">|</span><span>My Account</span><span class="sep">|</span><span>View Cart</span></nav>

<main class="cols">
  <aside class="col left">
    <section class="panel">
      <div class="panel-head"><span class="ico"></span>Currency</div>
      <div class="panel-body"><div class="select">U.S. Dollar (USD)<span>▾</span></div></div>
    </section>
    <section class="panel">
      <div class="panel-head"><span class="ico"></span>Categories</div>
      <div class="panel-body">
        <ul class="links">
          <li>New Products</li><li>Specials</li><li>Featured</li><li>Bestsellers</li>
          <li>Books &amp; Magazines</li><li>Movies, Music &amp; Games</li><li>Digital Downloads</li>
          <li>Computers &amp; Office</li><li>Electronics</li><li>Sports &amp; Outdoors</li>
        </ul>
      </div>
    </section>
    <section class="panel">
      <div class="panel-head"><span class="ico"></span>Manufacturers</div>
      <div class="panel-body"><div class="select">Select a Manufacturer<span>▾</span></div></div>
    </section>
    <section class="panel">
      <div class="panel-head"><span class="ico"></span>Bestsellers</div>
      <div class="panel-body">
        <ul class="links small">
          <li>Blue Gift Basket Deluxe Set</li><li>Power Supply Unit Pro</li><li>Wireless Mouse and Pad</li>
          <li>Mini Gift Box Wrap</li><li>Widescreen Desk Monitor</li><li>Gaming Headset Plus</li>
          <li>Image Print Set 10 Pack</li><li>Digital Gift Card Bundle</li><li>Classic Crystal Award Trophy</li>
        </ul>
      </div>
    </section>
    <section class="panel">
      <div class="panel-head"><span class="ico"></span>Site Information</div>
      <div class="panel-body">
        <ul class="links small">
          <li>Gift Registry</li><li>Gift Certificates</li><li>Privacy Policy</li>
          <li>About Us</li><li>Contact Us</li><li>Site Map</li>
        </ul>
      </div>
    </section>
    <section class="panel">
      <div class="panel-head"><span class="ico"></span>Newsletter Signup</div>
      <div class="panel-body center-text">
        <p style="font-weight:700;font-size:14px;line-height:1.45;margin-bottom:14px">Submit your e-mail address to receive free updates and promotions.</p>
        <div class="field">Enter your email</div>
        <span class="btn">Join</span>
      </div>
    </section>
  </aside>

  <section class="col center">
    <section class="panel">
      <div class="panel-head">Featured Products</div>
      <div class="product-list">
        <article class="product">
          <div class="thumb"><div class="photo" role="img" aria-label="Crystal award with lit base"></div><div class="sku">SKU: 12-34-74</div><div class="stars">★★★<span class="off">★★</span></div><div class="stock">In Stock</div></div>
          <div class="info"><h3>Laser Spot Crystals With Light Up Base</h3><p>Light Up Your Awards Presentation With This Breathtaking Laser Spot Crystal Award. This Genuine Crystal Award Features A Black Light Up Base That Illuminates The Crystal In Rotating Colors From Blue To Green To Yellow To Red. Choose From Our Highly Sets.</p><div class="price">$11.95</div><div class="actions"><span class="btn">Add to Cart</span><span class="btn ghost">More Info</span></div></div>
        </article>
        <article class="product">
          <div class="thumb"><div class="photo" role="img" aria-label="Crystal award with lit base"></div><div class="sku">SKU: 12-34-74</div><div class="stars">★★★<span class="off">★★</span></div><div class="stock">In Stock</div></div>
          <div class="info"><h3>Laser Spot Crystals With Light Up Base</h3><p>Light Up Your Awards Presentation With This Breathtaking Laser Spot Crystal Award. This Genuine Crystal Award Features A Black Light Up Base That Illuminates The Crystal In Rotating Colors From Blue To Green To Yellow To Red. Choose From Our Highly Sets.</p><div class="price">$11.95</div><div class="actions"><span class="btn">Add to Cart</span><span class="btn ghost">More Info</span></div></div>
        </article>
        <article class="product">
          <div class="thumb"><div class="photo" role="img" aria-label="Crystal award with lit base"></div><div class="sku">SKU: 12-34-74</div><div class="stars">★★★<span class="off">★★</span></div><div class="stock">In Stock</div></div>
          <div class="info"><h3>Laser Spot Crystals With Light Up Base</h3><p>Light Up Your Awards Presentation With This Breathtaking Laser Spot Crystal Award. This Genuine Crystal Award Features A Black Light Up Base That Illuminates The Crystal In Rotating Colors From Blue To Green To Yellow To Red. Choose From Our Highly Sets.</p><div class="price">$11.95</div><div class="actions"><span class="btn">Add to Cart</span><span class="btn ghost">More Info</span></div></div>
        </article>
        <article class="product">
          <div class="thumb"><div class="photo" role="img" aria-label="Crystal award with lit base"></div><div class="sku">SKU: 12-34-74</div><div class="stars">★★★<span class="off">★★</span></div><div class="stock">In Stock</div></div>
          <div class="info"><h3>Laser Spot Crystals With Light Up Base</h3><p>Light Up Your Awards Presentation With This Breathtaking Laser Spot Crystal Award. This Genuine Crystal Award Features A Black Light Up Base That Illuminates The Crystal In Rotating Colors From Blue To Green To Yellow To Red. Choose From Our Highly Sets.</p><div class="price">$11.95</div><div class="actions"><span class="btn">Add to Cart</span><span class="btn ghost">More Info</span></div></div>
        </article>
        <article class="product">
          <div class="thumb"><div class="photo" role="img" aria-label="Crystal award with lit base"></div><div class="sku">SKU: 12-34-74</div><div class="stars">★★★<span class="off">★★</span></div><div class="stock">In Stock</div></div>
          <div class="info"><h3>Laser Spot Crystals With Light Up Base</h3><p>Light Up Your Awards Presentation With This Breathtaking Laser Spot Crystal Award. This Genuine Crystal Award Features A Black Light Up Base That Illuminates The Crystal In Rotating Colors From Blue To Green To Yellow To Red. Choose From Our Highly Sets.</p><div class="price">$11.95</div><div class="actions"><span class="btn">Add to Cart</span><span class="btn ghost">More Info</span></div></div>
        </article>
      </div>
    </section>

    <section class="panel">
      <div class="panel-head">Find us</div>
      <div class="social-card">
        <div class="page-row"><div class="sq"></div><div><b>Keystone Web Tools, Inc.</b><br><span class="like">Like Page</span></div></div>
        <p style="font-size:12px;color:var(--muted);margin-top:14px">Be the first of your friends to like this</p>
        <div class="faces"><i></i><i></i><i></i><i></i><i></i><i></i></div>
      </div>
    </section>

    <section class="panel">
      <div class="panel-head">Follow us</div>
      <div class="tweet"><div class="av"></div><div><b>Keystone Web Tools</b> <span class="handle">@keystonewebtools</span><p>Thank you to all who have served our country. <span class="tag">#ServiceDay</span>.</p></div></div>
      <div class="tweet"><div class="av"></div><div><b>Keystone Web Tools</b> <span class="handle">@keystonewebtools</span><p>Code Liner Helper 4.0 is now in development. The long overdue update will include a updated interface and new features. Stay tuned.</p></div></div>
    </section>
  </section>

  <aside class="col right">
    <section class="panel">
      <div class="panel-head"><span class="ico"></span>Search</div>
      <div class="panel-body">
        <div class="select" style="margin-bottom:10px">All Categories<span>▾</span></div>
        <div style="display:flex;gap:8px"><div class="field" style="flex:1;margin:0">Keywords</div><span class="btn">Go</span></div>
        <p class="note" style="margin:10px 0 0">Advanced Search</p>
      </div>
    </section>
    <section class="panel">
      <div class="panel-head"><span class="ico"></span>Cart Contents</div>
      <div class="panel-body center-text">
        <p class="note">Your cart is currently empty.</p>
        <p style="font-weight:700;margin:10px 0 14px">Subtotal: $0.00</p>
        <span class="btn full">View Cart &amp; Checkout</span>
      </div>
    </section>
    <section class="panel">
      <div class="panel-head"><span class="ico"></span>Login</div>
      <div class="panel-body center-text">
        <p class="note">User name</p><div class="field">Enter username</div>
        <p class="note">Password</p><div class="field">Enter password</div>
        <span class="btn full" style="margin-bottom:10px">Login</span>
        <span class="btn full" style="margin-bottom:10px">Create a Free Account</span>
        <p style="font-weight:700;color:var(--accent-dark)">Forgot Password?</p>
      </div>
    </section>
    <section class="panel">
      <div class="panel-head"><span class="ico"></span>Sale Item</div>
      <div class="panel-body center-text">
        <div class="sale-photo" role="img" aria-label="Sale product image"></div>
        <p style="font-size:13px">StyleWeek (1 Year Subscription)</p>
        <p style="color:var(--accent);font-weight:700;margin-top:6px">$19.99</p>
      </div>
    </section>
  </aside>
</main>

<footer class="footer">Demo BrightCart 4.0 Store © Copyright 2017 Demo BrightCart 4.0 Store</footer>
<div class="totop"></div>
<div class="powered">Powered by BrightCart "Shopping Cart Software"</div>
</body>
</html>
```